Website design for Cambridge based systematic hedge fund

We have run previous craftmosaic competitions to design our company logo, business cards and the styling of our presentation deck (see attached files).
As the final step we are looking to get a website designed that is thematically consistent with these existing elements of our branding.
You can find some of our competitors websites below:
https://www.quelmarsh.example/
https://www.fenloor.example/
https://www.pyvart.example/
https://www.dulvet.example/
https://www.orbelmfunds.example/
https://www.valtrigo.example/
https://www.meskilfunds.example/home
We would like to have a website that works well on both mobile devices and desktops. Either just as one page that can be scrolled down, with links at the top that skips to certain sections, or a few separate pages that can be navigated by a top menu.
It should look professional, we are not after lots of animations or unnecessary transitions, and in particular the website must be smooth to navigate. We would like to avoid having peoples of people, we are happy to make use of elements from the presentation (for example the style of the cover slide, or the section slides with the faded bridge in the background), or 'financial' style images.
We would like to have the following sections for now. For some of these some example text has been provided, final text may change but it will be of similar length. For the other sections we are happy to just have template text for now. At the moment we are mainly interested to see styles/layouts as words can be added easily afterwards:
1) We will need a disclaimer pop up the first time someone visits the site (see for example the meskilfunds example).
2) Top page - company name, then in larger text "Bringing AI and Statistical Inference to Financial Markets", and somewhere in smaller text "Harlow Vectors is a quantitative asset manager with the singular focus of delivering algorithmic strategies that work"
3) "About us" section: will describe us as a company, details our approach, company values, and explains the company logo.
Example text:
"We deliver consistent alpha across liquid markets through the application of proprietary IP in Bayesian inference, machine learning and artificial intelligence. We are a multi-disciplinary team founded by experienced finance professionals from premier institutions, leading academics from the Thornbury Stellar Unit at Ashmere College and world-class software engineers.
Our logo portrays a sillhoute of the lattice walkway at Ashmere College. Our unique scientific approach allows us to bridge cutting-edge mathematical research and computing expertise with financial knowledge to bring algorithmns that work to liquid markets"
4) Hiring section, detailing our culture, what we are looking for.
Example text:
"We are always looking for exceptional talent to join our entrepreneurial team. We are looking for individuals who are creative thinkers, can demonstrate analytical rigour and are passionate about the intersection of science, finance and technology.
We prioritise having a company culture that promotes sharing ideas in a safe, collaborative research environment. We make sure that every member of the team has the oppertunity to explore their own ideas through weekly 'innovation time', and ensure that everyone gets the support they need to continue to grow as individuals within the company."
5) A section for news/press releases
6) Contact us area at the bottom with office location and email. We will need to list 3 addresses for our Cambridge, London and Singapore offices, along with a couple of contact emails or phone numbers
7) A client login button at the top that will take them to a different website (unrelated to this one).

```html
<!DOCTYPE html>
<html lang="en">
<head>
<meta charset="utf-8">
<title>Harlow Vectors</title>
<link href="https://fonts.googleapis.com/css2?family=Montserrat:wght@300;500;600;700&family=Roboto:wght@300;400;500;700&display=swap" rel="stylesheet">
<style>
:root{
  --navy-deep:#07143f;
  --navy:#0c2a6b;
  --brand-blue:#0d3f78;
  --accent:#4a8fdb;
  --link:#2f73c9;
  --ink:#121826;
  --body:#6b7280;
  --pale:#eef5fd;
  --white:#ffffff;
}
*{box-sizing:border-box;margin:0;padding:0}
html,body{width:1200px;height:4926px;overflow:hidden}
body{position:relative;font-family:'Roboto',sans-serif;color:var(--ink);background:var(--white)}
.abs{position:absolute}
.heading{font-family:'Montserrat',sans-serif;font-weight:700;text-transform:uppercase;color:var(--ink)}
.btn{position:absolute;display:flex;align-items:center;justify-content:center;height:44px;font:700 13px 'Roboto',sans-serif;text-transform:uppercase;letter-spacing:.3px;border-radius:2px}
.btn-solid{background:var(--accent);color:var(--white);width:146px}
.btn-outline{border:2px solid var(--white);color:var(--white);width:146px}
.copy{font-size:13.5px;line-height:24px;color:var(--body)}

/* hero */
.hero{position:absolute;left:0;top:0;width:1200px;height:623px;background:linear-gradient(180deg,var(--navy-deep) 0%,var(--navy) 70%,#1a3f8c 100%);overflow:hidden}
.hero-ghost{position:absolute;left:300px;top:118px;font:700 120px 'Montserrat',sans-serif;color:rgba(255,255,255,.04);letter-spacing:6px}
.brand{position:absolute;color:var(--white);font-family:'Montserrat',sans-serif;font-weight:700;text-align:center}
.brand .name{display:block;font-size:28px;letter-spacing:1px;line-height:1}
.brand .sub{display:block;font-size:11px;letter-spacing:9px;margin-top:6px;font-weight:600}
.nav{position:absolute;top:36px;left:400px;display:flex;gap:0;font-size:15px;color:var(--white)}
.nav a{position:absolute;color:var(--white);text-decoration:none;white-space:nowrap}
.hero-title{position:absolute;left:99px;top:178px;font:700 44px/49px 'Montserrat',sans-serif;color:var(--white);width:520px}
.hero-lead{position:absolute;left:99px;top:342px;width:470px;font:500 17px/28px 'Roboto',sans-serif;color:var(--white)}
.hero-visual{position:absolute;left:650px;top:124px;width:397px;height:402px;border-radius:50%;background:radial-gradient(circle at 50% 45%,rgba(90,160,255,.55),rgba(30,90,220,.35) 55%,rgba(10,40,120,0) 72%)}
.scroll-cue{position:absolute;left:590px;top:580px}

/* about */
.about-label{left:99px;top:728px;font:500 14px 'Roboto',sans-serif;color:var(--brand-blue);text-transform:uppercase}
.about-title{left:99px;top:752px;font-size:34px}
.about-copy{left:99px;top:806px;width:520px}
.about-visual{left:598px;top:623px;width:602px;height:396px;background:linear-gradient(200deg,#dde9f8 0%,#f4f8fd 60%,#ffffff 100%)}
.pale-band{left:0;top:1424px;width:1200px;height:617px;background:var(--pale)}
.years{left:94px;top:1060px;font:300 132px/1 'Roboto',sans-serif;color:var(--ink)}
.years-label{left:99px;top:1219px;font:500 16px 'Roboto',sans-serif}
.years-copy{left:99px;top:1248px;width:350px;font-size:11.5px;line-height:22px;color:var(--body)}
.stats{left:598px;top:1019px;width:602px;height:472px;background:var(--white)}
.stat-num{position:absolute;width:190px;text-align:center;font:300 58px/1 'Roboto',sans-serif;color:var(--ink)}
.stat-num sup{font-size:30px;vertical-align:14px}
.stat-label{position:absolute;left:208px;font:500 16px 'Roboto',sans-serif}
.stat-copy{position:absolute;left:208px;width:300px;font-size:11.5px;line-height:22px;color:var(--body)}

/* approach */
.approach-title{left:99px;top:1528px;font-size:44px;line-height:48px}
.approach-copy{left:99px;top:1646px;width:410px;font-size:13.5px;line-height:24px;color:var(--body)}
.photo{position:absolute}
.approach-photo{left:629px;top:1533px;width:435px;height:466px;background:linear-gradient(135deg,#d9d4cc,#9aa3ad 55%,#5e6b78)}

/* values */
.values{left:0;top:2041px;width:1200px;height:696px;background:linear-gradient(180deg,#0e3a74,var(--brand-blue) 60%,#0b3567)}
.values-title{position:absolute;left:0;width:1200px;top:2134px;text-align:center;font:600 40px 'Montserrat',sans-serif;color:var(--white)}
.value{position:absolute;width:240px;text-align:center;color:var(--white)}
.value svg{display:block;margin:0 auto}
.value p{margin-top:18px;font:500 16px/19px 'Montserrat',sans-serif}

/* hiring */
.hiring-title{left:99px;top:2858px;font-size:33px;line-height:36px}
.hiring-copy{left:99px;top:2954px;width:478px;font-size:13px;line-height:24px;color:var(--body)}
.hiring-photo{left:625px;top:2828px;width:475px;height:463px;background:linear-gradient(120deg,#cfd5d8,#8e8a84 50%,#4b4540)}

/* press */
.press{left:0;top:3386px;width:1200px;height:608px;background:var(--pale)}
.press-title{position:absolute;left:0;width:1200px;top:3460px;text-align:center;font-size:34px}
.card{position:absolute;top:3535px;width:317px}
.card-photo{position:relative;height:218px}
.date{position:absolute;right:6px;top:6px;width:28px;height:52px;background:var(--brand-blue);color:var(--white);text-align:center;font:500 9px/13px 'Roboto',sans-serif;padding-top:2px}
.date b{display:block;font-size:14px}
.card h3{margin-top:25px;font:500 20px/24px 'Roboto',sans-serif;color:var(--ink)}
.card p{margin-top:8px;font-size:12.5px;line-height:23px;color:var(--body)}
.card a{display:block;margin-top:6px;font:500 11px 'Roboto',sans-serif;color:var(--link);text-decoration:underline;text-transform:uppercase}

/* contact */
.contact-photo{left:0;top:3994px;width:598px;height:529px;background:linear-gradient(200deg,#e9f1fa 0%,#7fa3cd 45%,#274f86 100%)}
.contact-title{left:667px;top:4080px;font-size:34px}
.office{position:absolute;font-size:12px;line-height:17px;color:var(--ink)}
.office h4{font:500 14.5px 'Roboto',sans-serif;text-transform:uppercase;display:flex;align-items:center;gap:8px;margin-left:-4px}
.office .addr{margin:6px 0 0 27px}
.office .row{display:flex;align-items:center;gap:10px;margin-top:10px}
.office .row span b{color:var(--link);font-weight:500}

/* footer */
.footer{left:0;top:4523px;width:1200px;height:403px;background:var(--brand-blue);color:var(--white)}
.social{position:absolute;width:34px;height:34px;border-radius:50%;background:#0a3265;border:1px solid rgba(255,255,255,.25)}
.foot-col{position:absolute;top:4606px;font-size:14px;line-height:28px;color:#dbe6f4}
.foot-col h5{font:600 15.5px 'Montserrat',sans-serif;color:var(--white);text-transform:uppercase;line-height:20px;margin-bottom:12px}
.copyright{position:absolute;left:0;width:1200px;top:4880px;text-align:center;font-size:13px;color:#dbe6f4}
</style>
</head>
<body>

<header class="hero">
  <div class="hero-ghost">HARLOW</div>
  <div class="brand" style="left:99px;top:40px;width:180px"><span class="name">HARLOW</span><span class="sub">VECTORS</span></div>
  <nav>
    <a class="nav" style="left:400px;top:36px">Home</a>
    <a class="nav" style="left:487px;top:36px">About Us</a>
    <a class="nav" style="left:602px;top:36px">Our Culture</a>
    <a class="nav" style="left:734px;top:36px">News</a>
    <a class="nav" style="left:818px;top:36px">Career</a>
    <a class="nav" style="left:911px;top:36px">Contact Us</a>
    <a class="nav" style="left:1015px;top:36px">|</a>
    <a class="nav" style="left:1041px;top:36px">
      <svg width="12" height="12" viewBox="0 0 12 12" style="vertical-align:-1px"><circle cx="6" cy="3.5" r="3" fill="#fff"/><path d="M0 12c0-4 3-5.5 6-5.5s6 1.5 6 5.5z" fill="#fff"/></svg> Login</a>
  </nav>
  <h1 class="hero-title">Bringing AI and Statistical Inference to Financial Markets</h1>
  <p class="hero-lead">Harlow Vectors is a quantitative asset manager with the singular focus of delivering algorithmic strategies that work</p>
  <a class="btn btn-solid" style="left:99px;top:443px">Get Started</a>
  <a class="btn btn-outline" style="left:260px;top:443px">Learn More</a>
  <div class="hero-visual" role="img" aria-label="Glowing blue network sphere illustration"></div>
  <svg class="scroll-cue" width="20" height="28" viewBox="0 0 20 28"><path d="M10 2v22M4 18l6 6 6-6" fill="none" stroke="#fff" stroke-width="1.5"/></svg>
</header>

<section>
  <div class="abs about-visual" role="img" aria-label="Blue network of connected nodes"></div>
  <p class="abs about-label">About Us</p>
  <h2 class="abs heading about-title">Harlow Vectors</h2>
  <p class="abs copy about-copy">We deliver consistent alpha across liquid markets through the application of proprietary IP in Bayesian inference, machine learning and artificial intelligence. We are a multi-disciplinary team founded by experienced finance professionals from premier institutions, leading academics from the Thornbury Stellar Unit at Ashmere College and world-class software engineers.</p>
  <a class="btn btn-solid" style="left:99px;top:950px">Learn More</a>

  <div class="abs pale-band"></div>
  <div class="abs years">20</div>
  <p class="abs years-label">Year History</p>
  <p class="abs years-copy">Lorem ipsum dolor sit amet, consectetur adipiscing elit, sed do eiusmod tempor incididunt ut labore etlore magna aliqua. Quis ipsum suspendisse ultrices gravida.</p>

  <div class="abs stats">
    <div class="stat-num" style="left:0;top:24px">200<sup>+</sup></div>
    <p class="stat-label" style="top:28px">Team Members</p>
    <p class="stat-copy" style="top:50px">Lorem ipsum dolor sit amet, consectetur adipiscing elit, sed do eiusmod tempor incididunt</p>
    <div class="stat-num" style="left:0;top:132px">60<sup>+</sup></div>
    <p class="stat-label" style="top:134px">Portfolio Managers</p>
    <p class="stat-copy" style="top:156px">Lorem ipsum dolor sit amet, consectetur adipiscing elit, sed do eiusmod tempor incididunt</p>
    <div class="stat-num" style="left:0;top:258px">07</div>
    <p class="stat-label" style="top:258px">Offices</p>
    <p class="stat-copy" style="top:280px">Lorem ipsum dolor sit amet, consectetur adipiscing elit, sed do eiusmod tempor incididunt</p>
  </div>
</section>

<section>
  <h2 class="abs heading approach-title">Our<br>Approach</h2>
  <div class="abs approach-copy">
    <p>Sed ut perspiciatis unde omnis iste natus error sit voluptatem accusantium doloremque laudantium, totam reperiam, eaque ipsa quae ab illo inventore veritatis et quasi architecto beatae vitae dicta sunt explicabo. Nemo enim ipsam voluptatem quia voluptas sit aspernatur</p>
    <p style="margin-top:21px">Sed ut perspiciatis unde omnis iste natus error sit voluptatem accusantium doloremque laudantium, totam reperiam, eaque ipsa quae ab illo inventore</p>
  </div>
  <a class="btn btn-solid" style="left:99px;top:1882px">Learn More</a>
  <div class="photo approach-photo" role="img" aria-label="Photo of a team meeting around an office table with laptops"></div>
</section>

<section>
  <div class="abs values"></div>
  <h2 class="values-title">OUR VALUES</h2>
  <div class="value" style="left:161px;top:2264px">
    <svg width="86" height="86" viewBox="0 0 86 86"><path d="M43 3l36 20v40L43 83 7 63V23z" fill="none" stroke="rgba(255,255,255,.35)" stroke-width="1.5"/><circle cx="43" cy="43" r="11" fill="none" stroke="#fff" stroke-width="1.6"/><path d="M43 37v12M39 40h8" stroke="#fff" stroke-width="1.6"/></svg>
    <p>Finibus Bonorum<br>et Malorum</p>
  </div>
  <div class="value" style="left:480px;top:2264px">
    <svg width="86" height="86" viewBox="0 0 86 86"><path d="M43 3l36 20v40L43 83 7 63V23z" fill="none" stroke="rgba(255,255,255,.35)" stroke-width="1.5"/><rect x="33" y="31" width="20" height="24" fill="none" stroke="#fff" stroke-width="1.6"/><path d="M37 38h12M37 43h12M37 48h8" stroke="#fff" stroke-width="1.6"/></svg>
    <p>Finibus Bonorum<br>et Malorum</p>
  </div>
  <div class="value" style="left:799px;top:2264px">
    <svg width="86" height="86" viewBox="0 0 86 86"><path d="M43 3l36 20v40L43 83 7 63V23z" fill="none" stroke="rgba(255,255,255,.35)" stroke-width="1.5"/><rect x="31" y="32" width="24" height="18" fill="none" stroke="#fff" stroke-width="1.6"/><path d="M35 46l5-5 4 3 7-7" fill="none" stroke="#fff" stroke-width="1.6"/><path d="M38 55h10" stroke="#fff" stroke-width="1.6"/></svg>
    <p>Finibus Bonorum<br>et Malorum</p>
  </div>
  <div class="value" style="left:161px;top:2489px">
    <svg width="86" height="86" viewBox="0 0 86 86"><path d="M43 3l36 20v40L43 83 7 63V23z" fill="none" stroke="rgba(255,255,255,.35)" stroke-width="1.5"/><path d="M32 54V44M38 54V38M44 54V41M50 54V34M30 55h24" stroke="#fff" stroke-width="1.6"/></svg>
    <p>Finibus Bonorum<br>et Malorum</p>
  </div>
  <div class="value" style="left:480px;top:2489px">
    <svg width="86" height="86" viewBox="0 0 86 86"><path d="M43 3l36 20v40L43 83 7 63V23z" fill="none" stroke="rgba(255,255,255,.35)" stroke-width="1.5"/><path d="M43 31l12 12-12 12-12-12z" fill="none" stroke="#fff" stroke-width="1.6"/><path d="M37 43h12" stroke="#fff" stroke-width="1.6"/></svg>
    <p>Finibus Bonorum<br>et Malorum</p>
  </div>
  <div class="value" style="left:799px;top:2489px">
    <svg width="86" height="86" viewBox="0 0 86 86"><path d="M43 3l36 20v40L43 83 7 63V23z" fill="none" stroke="rgba(255,255,255,.35)" stroke-width="1.5"/><rect x="32" y="38" width="22" height="16" fill="none" stroke="#fff" stroke-width="1.6"/><path d="M37 38v-5h12v5" fill="none" stroke="#fff" stroke-width="1.6"/><path d="M32 45h22" stroke="#fff" stroke-width="1.6"/></svg>
    <p>Finibus Bonorum<br>et Malorum</p>
  </div>
</section>

<section>
  <h2 class="abs heading hiring-title">What We Are<br>Looking For</h2>
  <div class="abs hiring-copy">
    <p>We are always looking for exceptional talent to join our entrepreneurial team. We are looking for individuals who are creative thinkers, can demonstrate analytical rigour and are passionate about the intersection of science, finance and technology.</p>
    <p style="margin-top:24px">We prioritise having a company culture that promotes sharing ideas in a safe, collaborative research environment. We make sure that every member of the team has the opportunity to explore their own ideas through weekly 'innovation time', and ensure that everyone gets the support they need to continue to grow as individuals within the company.</p>
  </div>
  <a class="btn btn-solid" style="left:99px;top:3213px">Learn More</a>
  <div class="photo hiring-photo" role="img" aria-label="Photo of a person working on a laptop by an office window"></div>
</section>

<section>
  <div class="abs press"></div>
  <h2 class="heading press-title">Press Releases</h2>
  <article class="card" style="left:86px">
    <div class="card-photo" role="img" aria-label="Photo of colleagues in a bright meeting room" style="background:linear-gradient(135deg,#e4ddd2,#9b8f80 60%,#4f4a44)"><div class="date">Aug<b>26</b>2021</div></div>
    <h3>Sed ut perspiciatis unde omnis iste natus error sit</h3>
    <p>Sed ut perspiciatis unde omnis iste natus error sit voluptatem accusantium doloremque laudantium, totam reperiam, eaque ipsa</p>
    <a>Learn More &raquo;</a>
  </article>
  <article class="card" style="left:428px">
    <div class="card-photo" role="img" aria-label="Photo of a trading floor with market screens" style="background:linear-gradient(135deg,#cfd9e2,#6f8596 55%,#2c3a46)"><div class="date">Aug<b>26</b>2021</div></div>
    <h3>Sed ut perspiciatis unde omnis iste natus error sit</h3>
    <p>Sed ut perspiciatis unde omnis iste natus error sit voluptatem accusantium doloremque laudantium, totam reperiam, eaque ipsa</p>
    <a>Learn More &raquo;</a>
  </article>
  <article class="card" style="left:770px">
    <div class="card-photo" role="img" aria-label="Illustration of AI and global finance symbols" style="background:linear-gradient(135deg,#5b6f86,#2f4259 55%,#1b2736)"><div class="date">Aug<b>26</b>2021</div></div>
    <h3>Sed ut perspiciatis unde omnis iste natus error sit</h3>
    <p>Sed ut perspiciatis unde omnis iste natus error sit voluptatem accusantium doloremque laudantium, totam reperiam, eaque ipsa</p>
    <a>Learn More &raquo;</a>
  </article>
</section>

<section>
  <div class="abs contact-photo" role="img" aria-label="Photo looking up at glass skyscrapers against a blue sky"></div>
  <h2 class="abs heading contact-title">Contact Us</h2>

  <div class="office" style="left:694px;top:4148px">
    <h4><svg width="14" height="18" viewBox="0 0 14 18"><path d="M7 0a7 7 0 0 0-7 7c0 5 7 11 7 11s7-6 7-11a7 7 0 0 0-7-7z" fill="#0d3f78"/><circle cx="7" cy="7" r="2.6" fill="#fff"/></svg>London</h4>
    <p class="addr">1234 Somestreet<br>Anywhere USA 21212</p>
    <div class="row"><svg width="14" height="14" viewBox="0 0 14 14"><path d="M3 1l2.5 3-1.5 2a8 8 0 0 0 4 4l2-1.5 3 2.5-1.5 2C6 13 1 8 1 2.5z" fill="#0d3f78"/></svg><span>Tel: <b>+888 888 8888</b></span></div>
    <div class="row"><svg width="14" height="11" viewBox="0 0 14 11"><rect width="14" height="11" fill="#0d3f78"/><path d="M0 0l7 6 7-6" fill="none" stroke="#fff" stroke-width="1.2"/></svg><span>Email: <b>info@harlowvectors.example</b></span></div>
  </div>

  <div class="office" style="left:923px;top:4148px">
    <h4><svg width="14" height="18" viewBox="0 0 14 18"><path d="M7 0a7 7 0 0 0-7 7c0 5 7 11 7 11s7-6 7-11a7 7 0 0 0-7-7z" fill="#0d3f78"/><circle cx="7" cy="7" r="2.6" fill="#fff"/></svg>Washington DC</h4>
    <p class="addr">1234 Somestreet<br>Anywhere USA 21212</p>
    <div class="row"><svg width="14" height="14" viewBox="0 0 14 14"><path d="M3 1l2.5 3-1.5 2a8 8 0 0 0 4 4l2-1.5 3 2.5-1.5 2C6 13 1 8 1 2.5z" fill="#0d3f78"/></svg><span>Tel: <b>+888 888 8888</b></span></div>
    <div class="row"><svg width="14" height="11" viewBox="0 0 14 11"><rect width="14" height="11" fill="#0d3f78"/><path d="M0 0l7 6 7-6" fill="none" stroke="#fff" stroke-width="1.2"/></svg><span>Email: <b>info@harlowvectors.example</b></span></div>
  </div>

  <div class="office" style="left:694px;top:4317px">
    <h4><svg width="14" height="18" viewBox="0 0 14 18"><path d="M7 0a7 7 0 0 0-7 7c0 5 7 11 7 11s7-6 7-11a7 7 0 0 0-7-7z" fill="#0d3f78"/><circle cx="7" cy="7" r="2.6" fill="#fff"/></svg>New York NY</h4>
    <p class="addr">1234 Somestreet<br>Anywhere USA 21212</p>
    <div class="row"><svg width="14" height="14" viewBox="0 0 14 14"><path d="M3 1l2.5 3-1.5 2a8 8 0 0 0 4 4l2-1.5 3 2.5-1.5 2C6 13 1 8 1 2.5z" fill="#0d3f78"/></svg><span>Tel: <b>+888 888 8888</b></span></div>
    <div class="row"><svg width="14" height="11" viewBox="0 0 14 11"><rect width="14" height="11" fill="#0d3f78"/><path d="M0 0l7 6 7-6" fill="none" stroke="#fff" stroke-width="1.2"/></svg><span>Email: <b>info@harlowvectors.example</b></span></div>
  </div>
</section>

<footer>
  <div class="abs footer"></div>
  <div class="brand" style="left:99px;top:4660px;width:240px"><span class="name" style="font-size:34px">HARLOW</span><span class="sub" style="font-size:13px;letter-spacing:12px">VECTORS</span></div>
  <span class="social" style="left:134px;top:4760px"></span>
  <span class="social" style="left:180px;top:4760px"></span>
  <span class="social" style="left:226px;top:4760px"></span>
  <span class="social" style="left:272px;top:4760px"></span>

  <div class="foot-col" style="left:480px">
    <h5>Quick Links</h5>
    Home<br>About Us<br>Our Culture<br>News<br>Career<br>Contact Us
  </div>
  <div class="foot-col" style="left:737px">
    <h5>How To Join</h5>
    Career Development<br>Choose Your Path<br>Interviewing<br>Internships<br>Upcoming Events<br>Fellowship Program<br>Application FAQ
  </div>
  <div class="foot-col" style="left:1009px">
    <h5>Careers</h5>
    Open Roles<br>Internships<br>Interview Tips
  </div>
  <p class="copyright">Copyright &copy; 2021 Harlow Vectors. All rights reserved.</p>
</footer>

</body>
</html>
```